Kavak Verbatics web design: a translation company with corporate clients

Need a new website for my translation and localization company with file uploading capacity directed to email for quotation

old (very old) web site is www.kvkaktarim.example you can use the content text there or lorem ipsum, We will provide the texts. It will be in English - Turkish - French and German
For the content and overall layout: https://www.pellardlanguages.example/

For the color scheme you'll need to see logo's colors.

I am rebranding so new logo is uploaded The new adress will be www.kavakverbatics.example

Target Market(s)

Primarily corporate clients

Industry/Entity Type

It Company

Coding

Coded - Design and coding required

Number of Pages Required

5+ page

Font styles to use
Other font styles liked:
• Calibri

Requirements
Must have
• References on homepage (logos will be sent during design phase)
• Services: Translation, Interpretation, Localization&Consultancy, Translation API
• Quotation Form and file uploading
• Simple layout evoking reliability, speed and accuracy
Nice to have
• For the content and overall layout: https://www.pellardlanguages.example/
• Separate page for Translation Services: Marketing Translation, Legal Translation, Technical Translation, Personal Translation
• and texts under these headings
Should not have
• Old style
• Complex design

```html
<!DOCTYPE html>
<html lang="en">
<head>
<meta charset="utf-8">
<title>Kavak Verbatics – Translation, Localization &amp; Consultancy</title>
<link rel="stylesheet" href="https://fonts.googleapis.com/css2?family=Roboto:wght@300;400;500;700&display=swap">
<style>
:root{
  --olive:#6b7651;
  --olive-dark:#4a5a2a;
  --orange:#e38a2b;
  --text:#6f6f6f;
  --heading:#333333;
  --light:#f1f1f1;
  --footer:#333333;
  --footer-line:#444444;
  --white:#ffffff;
}
*{box-sizing:border-box;margin:0;padding:0}
html,body{width:1200px;height:2517px;overflow:hidden}
body{font-family:"Roboto",Arial,sans-serif;color:var(--text);background:var(--white)}
.top-bar{height:50px;background:var(--olive);position:relative}
.lang-button{position:absolute;left:958px;top:0;width:144px;height:50px;background:var(--orange);color:var(--white);font-size:15px;display:flex;align-items:center;justify-content:center;gap:10px}
.site-header{height:98px;position:relative;border-bottom:1px solid #e6e6e6}
.brand{position:absolute;left:100px;top:29px;display:flex;align-items:center;gap:12px}
.brand-dot{width:40px;height:40px;border-radius:50%;background:var(--orange)}
.brand-name{font-size:26px;font-weight:500;color:var(--olive-dark);letter-spacing:.5px}
.main-nav{position:absolute;right:100px;top:0;height:98px;display:flex;align-items:center;gap:46px;list-style:none}
.main-nav li{font-size:13px;color:#555;text-transform:uppercase;letter-spacing:.3px}
.main-nav li.active{color:var(--orange)}
.hero{height:595px;position:relative;background:linear-gradient(100deg,#5e7c92 0%,#8fa8b8 45%,#b7c6cf 70%,#7f98aa 100%)}
.hero-title{position:absolute;left:0;right:0;top:192px;text-align:center;color:var(--white);font-size:46px;font-weight:700;letter-spacing:.3px;line-height:56px}
.hero-arrow{position:absolute;top:197px;width:46px;height:46px;border-radius:50%;background:rgba(255,255,255,.45);display:flex;align-items:center;justify-content:center}
.hero-arrow.prev{left:27px}.hero-arrow.next{left:1123px}
.welcome{height:269px;border-bottom:1px solid #e9e9e9;text-align:center;padding-top:38px}
.welcome h1{font-size:28px;font-weight:700;color:var(--orange);text-transform:uppercase}
.welcome h1 span{color:var(--olive-dark)}
.welcome p{width:820px;margin:0 auto;font-size:14px;line-height:25px}
.welcome p:first-of-type{margin-top:22px}
.welcome p+p{margin-top:11px}
.services{height:448px;position:relative}
.section-title{font-size:28px;font-weight:700;text-transform:uppercase}
.services .section-title{position:absolute;left:100px;top:34px;color:var(--olive-dark)}
.section-title .accent{color:var(--orange)}
.slider-arrows{position:absolute;left:1052px;top:42px;display:flex;gap:3px}
.slider-arrows span{width:21px;height:21px;background:var(--orange);display:flex;align-items:center;justify-content:center}
.service-cards{position:absolute;left:100px;top:97px;display:flex;gap:17px}
.service-card{width:237px;height:292px;border:1px solid #e3e3e3;text-align:center;padding:3px}
.service-image{height:158px}
.service-card h3{font-size:16px;font-weight:400;color:var(--heading);margin-top:17px;text-transform:uppercase;letter-spacing:.2px}
.service-card p{font-size:13px;line-height:25px;color:#999;margin-top:8px;padding:0}
.service-image.marketing{background:linear-gradient(135deg,#e9ecef,#c9d3db)}
.service-image.legal{background:linear-gradient(135deg,#7a4a35,#b9786a 60%,#8c99b3)}
.service-image.technical{background:linear-gradient(135deg,#efeae4,#c9c4bd)}
.service-image.personal{background:linear-gradient(135deg,#d8d2cc,#a89f98)}
.team{height:567px;background:var(--olive);position:relative;text-align:center}
.team .section-title{padding-top:33px;color:var(--white)}
.team-intro{width:700px;margin:14px auto 0;font-size:14px;line-height:25px;color:#eef0e6}
.team-grid{position:absolute;left:100px;top:174px;display:flex;gap:17px}
.member{width:237px}
.member-photo{height:226px;border:2px solid var(--white)}
.member-photo.m1{background:linear-gradient(160deg,#d9d9d9,#9a8a80)}
.member-photo.m2{background:linear-gradient(160deg,#e4e4e4,#a58f80)}
.member-photo.m3{background:linear-gradient(160deg,#cfcfcf,#8a7a70)}
.member-photo.m4{background:linear-gradient(160deg,#d8c3bb,#b24a3c)}
.member h4{color:var(--orange);font-size:15px;font-weight:400;margin-top:14px}
.member p{color:var(--white);font-size:13.5px;line-height:23px;margin-top:10px;padding:0 12px}
.clients{height:164px;background:var(--light);position:relative;text-align:center}
.clients-lead{padding-top:38px;color:var(--orange);font-size:17px}
.client-row{position:absolute;left:100px;right:100px;top:90px;display:flex;align-items:center;justify-content:space-between}
.client-name{font-size:27px;font-weight:500;color:#a3a3a3;letter-spacing:.5px}
.client-arrow{width:14px}
.site-footer{height:262px;background:var(--footer);position:relative}
.footer-col{position:absolute;top:38px;height:190px}
.footer-col h5{font-size:14px;font-weight:700;color:var(--orange);text-transform:uppercase}
.footer-col p{font-size:12px;line-height:22px;color:#cfcfcf}
.col-about{left:100px;width:220px}
.col-features{left:344px;width:240px;padding-left:20px;border-left:1px solid var(--footer-line)}
.col-follow{left:604px;width:238px;padding-left:22px;border-left:1px solid var(--footer-line)}
.col-contact{left:862px;width:240px;padding-left:24px;border-left:1px solid var(--footer-line)}
.footer-brand{display:flex;align-items:center;gap:10px;margin-top:16px}
.footer-brand .brand-dot{width:30px;height:30px}
.footer-brand .brand-name{font-size:20px;color:#6d7458}
.col-about p{margin-top:26px}
.col-features p{margin-top:16px;width:206px}
.col-features p+p{margin-top:12px}
.social{display:flex;gap:8px;margin-top:27px}
.social span{width:35px;height:35px;border-radius:50%;border:2px solid var(--white)}
.contact-list{list-style:none;margin-top:14px}
.contact-list li{display:flex;gap:12px;font-size:12px;line-height:22px;color:#cfcfcf;margin-bottom:4px}
.contact-list svg{flex:none;margin-top:5px}
.bottom-bar{height:64px;background:var(--orange);position:relative;color:var(--white);font-size:13px;display:flex;align-items:center;justify-content:center}
.bottom-bar .code{position:absolute;right:100px}
</style>
</head>
<body>
<div class="top-bar">
  <div class="lang-button">Languages
    <svg width="9" height="6" viewBox="0 0 9 6"><path d="M1 1l3.5 3.5L8 1" fill="none" stroke="#fff" stroke-width="1.5"/></svg>
  </div>
</div>

<header class="site-header">
  <div class="brand"><span class="brand-dot"></span><span class="brand-name">Kavak Verbatics</span></div>
  <ul class="main-nav">
    <li class="active">Home</li><li>Our Services</li><li>Translation</li><li>Graphics Design</li><li>References</li><li>Contact Us</li>
  </ul>
</header>

<section class="hero" role="img" aria-label="Woman touching a digital world map interface with data graphics">
  <div class="hero-arrow prev"><svg width="14" height="20" viewBox="0 0 14 20"><path d="M11 2L3 10l8 8" fill="none" stroke="#fff" stroke-width="3"/></svg></div>
  <h2 class="hero-title">DELIVERY ON TIME WITH PERFECT QUALITY</h2>
  <div class="hero-arrow next"><svg width="14" height="20" viewBox="0 0 14 20"><path d="M3 2l8 8-8 8" fill="none" stroke="#fff" stroke-width="3"/></svg></div>
</section>

<section class="welcome">
  <h1>Hello and welcome to <span>Kavak Verbatics</span></h1>
  <p>KVK Translation Services meets the requirements of various organizations working in legal, finance, marketing and advertisement, technical and medical sectors with its expert, qualified translators.</p>
  <p>Our translation staff consists of language specialists who are all experts in their fields. By implementing the most appropriate visual ideas, we develop designing and printing stages of all kinds of corporate identity, advertisement, publicity and marketing documents which will raise awareness and serve the branding process.</p>
</section>

<section class="services">
  <h2 class="section-title"><span class="accent">Translation</span> Services</h2>
  <div class="slider-arrows">
    <span><svg width="8" height="10" viewBox="0 0 8 10"><path d="M6 1L2 5l4 4" fill="none" stroke="#fff" stroke-width="2"/></svg></span>
    <span><svg width="8" height="10" viewBox="0 0 8 10"><path d="M2 1l4 4-4 4" fill="none" stroke="#fff" stroke-width="2"/></svg></span>
  </div>
  <div class="service-cards">
    <article class="service-card">
      <div class="service-image marketing" role="img" aria-label="Businessman reviewing charts with a calculator"></div>
      <h3>Marketing Translation</h3><p>Translated documents are delivered in the required format</p>
    </article>
    <article class="service-card">
      <div class="service-image legal" role="img" aria-label="Judge's gavel in front of a flag"></div>
      <h3>Legal Translation</h3><p>Translated documents are delivered in the required format</p>
    </article>
    <article class="service-card">
      <div class="service-image technical" role="img" aria-label="Hands working with a computer mouse and keyboard"></div>
      <h3>Technical Translation</h3><p>Translated documents are delivered in the required format</p>
    </article>
    <article class="service-card">
      <div class="service-image personal" role="img" aria-label="Hand signing a document with a pen"></div>
      <h3>Personal Translation</h3><p>Translated documents are delivered in the required format</p>
    </article>
  </div>
</section>

<section class="team">
  <h2 class="section-title">Our Team <span class="accent">Members</span></h2>
  <p class="team-intro">Customer satisfaction is the focus of all our projects with our concept of service meeting the requirements of international standards.</p>
  <div class="team-grid">
    <div class="member"><div class="member-photo m1" role="img" aria-label="Portrait of team member Talin Moreau"></div><h4>Talin Moreau</h4><p>Our translation staff consists of language specialists who are all experts in their fields.</p></div>
    <div class="member"><div class="member-photo m2" role="img" aria-label="Portrait of team member Elsa Varga"></div><h4>Elsa Varga</h4><p>Our translation staff consists of language specialists who are all experts in their fields.</p></div>
    <div class="member"><div class="member-photo m3" role="img" aria-label="Portrait of team member Deniz Aydan"></div><h4>Deniz Aydan</h4><p>Our translation staff consists of language specialists who are all experts in their fields.</p></div>
    <div class="member"><div class="member-photo m4" role="img" aria-label="Portrait of team member Nora Lindqvist"></div><h4>Nora Lindqvist</h4><p>Our translation staff consists of language specialists who are all experts in their fields.</p></div>
  </div>
</section>

<section class="clients">
  <p class="clients-lead">Since 1999 more than 20,000 customers have trusted our translation services</p>
  <div class="client-row">
    <svg class="client-arrow" width="10" height="16" viewBox="0 0 10 16"><path d="M8 2L2 8l6 6" fill="none" stroke="#999" stroke-width="2"/></svg>
    <span class="client-name">SWIFTA</span>
    <span class="client-name">Corvane</span>
    <span class="client-name">AMBASSY</span>
    <span class="client-name">Lumora</span>
    <span class="client-name">teal</span>
    <span class="client-name">DURVEK</span>
    <svg class="client-arrow" width="10" height="16" viewBox="0 0 10 16"><path d="M2 2l6 6-6 6" fill="none" stroke="#999" stroke-width="2"/></svg>
  </div>
</section>

<footer class="site-footer">
  <div class="footer-col col-about">
    <h5>About Us</h5>
    <div class="footer-brand"><span class="brand-dot"></span><span class="brand-name">Kavak Verbatics</span></div>
    <p>Our translation staff consists of language specialists who are all experts in their fields.</p>
  </div>
  <div class="footer-col col-features">
    <h5>Features</h5>
    <p>Translated documents are delivered in the required format. Our motto is "Delivery on Time with Perfect Quality".</p>
    <p>Aside from English, translation services in all European and CIS languages.</p>
  </div>
  <div class="footer-col col-follow">
    <h5>Follow Us</h5>
    <div class="social"><span></span><span></span><span></span><span></span><span></span></div>
  </div>
  <div class="footer-col col-contact">
    <h5>Contact Us</h5>
    <ul class="contact-list">
      <li><svg width="9" height="12" viewBox="0 0 9 12"><path d="M4.5 0A4.5 4.5 0 0 0 0 4.5C0 8 4.5 12 4.5 12S9 8 9 4.5A4.5 4.5 0 0 0 4.5 0zm0 6.3a1.8 1.8 0 1 1 0-3.6 1.8 1.8 0 0 1 0 3.6z" fill="#fff"/></svg><span>Office: Lale Sok. Kavak Apt. No. 3 Daire 2 Çamlıtepe, 34500</span></li>
      <li><svg width="9" height="12" viewBox="0 0 9 12"><rect x="1" y="0" width="7" height="12" rx="1.5" fill="#fff"/><rect x="2.3" y="1.5" width="4.4" height="7.5" fill="#333"/></svg><span>Mobile: 0 212 555 0148</span></li>
      <li><svg width="11" height="11" viewBox="0 0 11 11"><rect x="0" y="4" width="11" height="7" rx="1" fill="#fff"/><rect x="2.5" y="0" width="6" height="5" fill="#fff"/></svg><span>Fax: 0 212 555 0179</span></li>
      <li><svg width="11" height="9" viewBox="0 0 11 9"><rect width="11" height="9" rx="1" fill="#fff"/><path d="M0.5 1l5 4 5-4" fill="none" stroke="#333" stroke-width="1.2"/></svg><span>Mail: info@kvkaktarim.example</span></li>
    </ul>
  </div>
</footer>

<div class="bottom-bar">KAVAK VERBATICS. © 2016 | Privacy Policy<span class="code">C16</span></div>
</body>
</html>
```